We need a web design for our business in which we provide complete network packages.

Hello Designers!

First, we’d like to make clear that rather than simple web design contents. We want someone that can help design our visual branding, help us communicate a sentiment. And we are willing to pay for that.

Who are we?

We are Harbor Lumen. Our company is based in Rotterdam, the Netherlands. We are providing a unique full-service concept for (wireless) communication networks within small to mid-range businesses. This means we will not only provide the hardware needed for a fast and secure network within a company, but will also install, optimize, support and maintain it. 

Harbor Lumen is a new brand of a company called Vector Lumen which has over 15 years of experience in the market of customer service and support. Harbor Lumen is the first satellite of more to come. Like Gear Lumen and others Planets, all have a focus on full service solutions.

Harbor Lumen has an experienced support center from which we can monitor our clients network in real time. Our clients don’t have to worry about anything, if something is not working correctly, we will fix it pro actively. Our clients range from education and training facilities, catering, industry, logistics, health care, consultancy agencies and high end consumers. 

In an overview all Unique Selling Points of Harbor Lumen:
• Professional service, both on location and remote!
• Direct clear price indication via our unique business configuration wizard
• A specific and complete quotation after a personal intake, within two days.
• Backed by a professional call center open 12 hours a day and open on Saturdays as well.
• Backed by a professional repair center with more than 15 years of experience.
• Installation and configuration included.
• Optimization included within the first three months powered by AI and machine learning.
• Real time remote maintenance. Quality control, security and interference.

Logo
For our business we need a logo. The logo needs to tell what we stand for and what we do. It will be used in both online and offline communication to our customers. Mainly e-mail and digital forms. As Harbor Lumen is one of the branches within our company we would like the logo to be part of a series in the future, which should be recognizable as part of a group of websites/brands.

Website
For our business we need a website.  The website needs a story and matching design and this is where you come in. The main focus of this website is to provide information, but more importantly to guide the user to our special quotation business configuration wizard. This business configuration wizard allows users to fill in information about their business and wish requirements, at which they will receive a real time price indication on completion. 

Configuration wizard
This business configuration wizard is developed separately by our own development team but should be part of the website in look and feel.. Our development team will develop the business configuration wizard and embed it in the website. 
The setup of the website should be focused on leading all visitors to the business configuration wizard which we create our quality leads. The website will inform the possible customers/leads on the unique selling points and then remind the customer to use the business configuration wizard to get a direct price indication. 

For the website and logo we need the whole package, the design you are creating needs to have returning elements like fonts, icons, color use,  images, maybe even characters etc. You name it! 
There needs to be a common thread in the design so we can reuse elements in, for example, the email templates, the work order or receipt we give to our customers (we may contact the winner of the contest to design these for us as well!). 

The layout needs to be complete. We want something modern. A one page design that is bright and colorful with collapsing area’s to show more information. 

Website wishes and requirements
The process:
The main function of our website, besides giving a clear indication what we do, will be to guide the user to our ‘business configuration wizard’. 

Website functionality:
Our website will be our main form of communication. We need a main/front page designed in a long single scrolling page style. Users can click on buttons to view more information. Information that was hidden before. We have included our own temporary mock ups to give you an idea of the flow we desire for the website. The titles and headers in these mock ups are in Dutch but we will translate this in the description below. These mock ups are just that, an idea about the visual presentation. You are free to implement your own design, fonts, icons, pictures etc.

The page will have 6 different areas (beside the top ‘hero’ part) and a final 7th area which is the “end page” and is a big business configuration wizard promotion.In each area you are pointed towards the business configuration wizard but if you scroll all the way down you will end up with this 7th area which is all about the wizard. However these 6 areas will need to be ‘expandable/collapsible’, meaning the user can click a “read more” button at which the element will expand to show extra information beneath it. The user can then collapse this element again by closing the part that just opened.

1. Top/Hero - Customers will be able to configure their own price indication through our wizard. So there will need to be a prominent button at the top of our main page and on the 7th area that will bring the customer to this wizard/application. This will need to be a focus throughout the whole website, meaning this button is a returning element. Furthermore the top needs two menus. One for navigating the main page itself, the other one is for switching between the different industry ‘flavors’ (Education, Logistics, Health Care etc). The idea is that the photos and text on the website will change depending on the industry picked. The design and layout remains the same however. The mock ups are based on ‘education’ and another based on logistics.

2. Real time Maintenance (Beheer) – This will be a collapsible component. It will provide a brief description of our maintenance service. The ‘configure now!’ button will need to be displayed in this area as well. This component is collapsible, meaning the user can click on a ‘Read more’ (Dutch: lees meer) button at which the element will open up to show extra information (2.1).
2.1 The extra information that can be collapsed by clicking the ‘X’ button. The headers on this page read “Carefree real time maintenance”, “Certified team of administrators”, “High service level”, “Defects immediately detected”, “Continuous remote maintenance”.

3.  Service range (Bereik) - This will be a collapsible component. It will provide a brief description of how we provide for enough wifi range within a building or company. The ‘configure now!’ button will need to be displayed in this area as well. This component is collapsible, meaning the user can click on a ‘Read more’ (Dutch: lees meer) button at which the element will open up to show extra information (3.1).
3.1 The extra information that can be collapsed by clicking the ‘X’ button. The headers on this page read “Enough range everywhere”, “Machine learning for maximum range”, “Different types of access points”, “Beamforming & Mu-MiMo”, “Multiple locations connected”.

4. Speed (Snelheid) -  This is the only component that needs to collapse twice. It will provide a brief description of how we will guarantee the fastest network speed possible. The ‘configure now!’ button will need to be displayed in this area as well. This component is collapsible, meaning the user can click on a ‘Read more’ (Dutch: lees meer) button at which the element will open up to show extra information (4.1).
4.1 The extra information that can be collapsed by clicking the ‘X’ button. The headers on this page read “Band steering, “Airtime fairness”, “Load balancing”. The user will be able to open up another element to show even more information (4.2).
4.2 This will mainly show the diagrams shown in the mock ups. It will provide extra information on what is meant by “Airtime fairness” and “Load balancing”.

5.  Manageable Costs (Beheersbare kosten) - This will be a collapsible component. It will provide a brief description of how users can manage their own costs. The ‘configure now!’ button will need to be displayed in this area as well. This component is collapsible, meaning the user can click on a ‘Read more’ (Dutch: lees meer) button at which the element will open up to show extra information (5.1).
5.1 The extra information that can be collapsed by clicking the ‘X’ button. The headers on this page read “Manageable costs”, “Upfront insight in predicated costs”, “Best price/quality ratio”, “10 years of warranty”, “High availability”.

6.  Protected and secure (Beschermd en veilig) -  This will be a collapsible component. It will provide a brief description of our protection and security guaranties. The ‘configure now!’ button will need to be displayed in this area as well. This component is collapsible, meaning the user can click on a ‘Read more’ (Dutch: lees meer) button at which the element will open up to show extra information (6.1).
6.1 The extra information that can be collapsed by clicking the ‘X’ button. The headers on this page read “Protected and Secure”, “Protected by Kelvo”, “Fire resistant and dust free”, “Managed and maintained in the Netherlands”.

7. Extras (Extra’s) - This will be a collapsible component. It will provide a brief description of additional options which our solution can provide. The ‘configure now!’ button will need to be displayed in this area as well. This component is collapsible, meaning the user can click on a ‘Read more’ (Dutch: lees meer) button at which the element will open up to show extra information (7.1).
7.1 The extra information that can be collapsed by clicking the ‘X’ button. The headers on this page read “Connection with portals like Chatloom”, “Everything in one cable”, “Cloud ready”, “Ready for even more?”.

8. unique business configuration wizard - This is the final page to (once again!) push the visitor to the ‘configure now!’ button showing some reasons to click right now.

For now, we need a logo and a website designed. We would also like a design for the configuration wizard in the same style as the website.

What we'd like:
- A modern professional, but fun, appearance
- Elements like icons to have a flat design.
- Website can be used for the different industry flavors (for example, our mockups are geared towards clients in the education sector, but we can simply swap some of the photos and content to reflect the health care sector).
- Keep in mind that the website will need to be responsive when designing!
- Create a fun and trustworthy feeling.

We will be able to provide stock photographs if necessary!

```html
<!DOCTYPE html>
<html lang="en">
<head>
<meta charset="utf-8">
<title>Harbor Lumen – Managed Wireless Networks</title>
<link rel="stylesheet" href="https://fonts.googleapis.com/css2?family=Poppins:wght@400;500&family=Roboto:wght@300;400;500;700&display=swap">
<style>
:root{
  --blue:#1e90f0;
  --navy:#1b2f5e;
  --text:#3e4756;
  --mist:#f1f7fb;
  --line:#d9e3ec;
  --white:#ffffff;
}
*{margin:0;padding:0;box-sizing:border-box}
a{text-decoration:none}
html,body{width:1200px;height:3681px;overflow:hidden;background:var(--white)}
body{position:relative;font-family:"Roboto",sans-serif;color:var(--text)}
.backdrop{position:absolute;left:0;top:0;width:1200px;height:3681px}

/* header */
.site-header{position:absolute;left:0;top:0;width:1200px;height:74px;background:var(--white);box-shadow:0 2px 8px rgba(20,50,90,.06);z-index:3}
.brand{position:absolute;left:231px;top:22px;display:flex;align-items:center;gap:10px;font-family:"Roboto",sans-serif;font-weight:500;font-size:21px;color:var(--blue)}
.brand-mark{width:26px;height:26px;border-radius:4px;background:currentColor}
.main-nav{position:absolute;left:644px;top:29px;display:flex;gap:38px;font-family:"Poppins",sans-serif;font-size:12.5px}
.main-nav a{color:var(--navy);padding-bottom:4px}
.main-nav a.is-active{color:var(--blue);border-bottom:1px solid var(--blue)}
.header-cta{position:absolute;left:800px;top:21px;width:171px;height:32px;border-radius:16px;background:var(--blue);color:var(--white);font-family:"Poppins",sans-serif;font-size:13px;display:flex;align-items:center;justify-content:center}

/* hero */
.hero{position:absolute;left:0;top:74px;width:1200px;height:442px}
.hero-photo{position:absolute;left:0;top:0;width:670px;height:442px;background:
  linear-gradient(180deg,rgba(255,255,255,0) 70%,rgba(220,226,232,.9) 100%),
  linear-gradient(100deg,#ece6dc 0%,#d6c6b0 18%,#b44a3a 30%,#d9b79a 42%,#f2efe9 52%,#8c9bb2 62%,#dfe2e8 74%,#c9cfd8 100%)}
.hero-panel{position:absolute;left:0;top:0;width:1200px;height:435px}
.hero-copy{position:absolute;left:600px;width:400px;top:156px;text-align:center;color:var(--white)}
.hero-title{font-weight:500;font-size:27px;line-height:40px;letter-spacing:.2px}
.hero-sub{font-weight:300;font-size:13.5px;margin-top:12px;opacity:.95}
.hero .cta-button{left:106px;top:127px;width:184px;height:33px}
.hero .cta-button .cta-label{background:var(--white);color:var(--blue)}

/* configure button */
.cta-button{display:block;position:absolute}
.cta-label{position:absolute;left:14px;right:0;top:0;bottom:0;border-radius:17px;background:var(--blue);color:var(--white);font-size:15px;display:flex;align-items:center;justify-content:center;padding-left:18px}
.cta-icon{position:absolute;left:0;top:50%;transform:translateY(-50%);width:36px;height:36px;border-radius:50%;background:var(--white);box-shadow:0 2px 6px rgba(30,80,150,.18);display:flex;align-items:center;justify-content:center;z-index:1}

/* features */
.feature{position:absolute;left:0;width:1200px;height:0}
.feature-title{position:absolute;top:-15px;font-weight:300;font-size:20px;line-height:30px;color:var(--navy);white-space:nowrap}
.feature-title strong{font-weight:700}
.feature-text{position:absolute;top:40px;width:380px;font-weight:300;font-size:11.6px;line-height:26.2px;color:var(--text)}
.feature .cta-button{top:171px;width:177px;height:30px}
.feature-divider{position:absolute;top:-27px;width:1px;height:280px;background:var(--line)}
.feature-art{position:absolute;border-radius:22px}
.read-more{position:absolute;top:250px;width:126px;height:31px;border:1px solid #c7d3df;background:var(--white);color:#5a6f8a;font-size:13px;display:flex;align-items:center;justify-content:center;gap:6px}
.read-more span{font-size:16px;color:#7a8ba0;line-height:1}

.feature--left .feature-title,.feature--left .feature-text{left:232px}
.feature--left .cta-button{left:240px}
.feature--left .feature-divider{left:667px}
.feature--left .read-more{left:608px}

.feature--right .feature-title,.feature--right .feature-text{left:603px}
.feature--right .cta-button{left:610px}
.feature--right .feature-divider{left:550px}
.feature--right .read-more{left:487px}

.art-maintenance{left:729px;top:31px;width:267px;height:143px;background:linear-gradient(135deg,#e3ecfb 0%,#9dbcef 45%,#5f8fe0 70%,#f3a64b 100%)}
.art-range{left:169px;top:26px;width:314px;height:150px;background:linear-gradient(120deg,#f6a33a 0%,#c9dbf7 25%,#8fb0ea 55%,#3b5fa8 80%,#f39a3c 100%)}
.art-speed{left:750px;top:6px;width:230px;height:207px;background:linear-gradient(150deg,#d9f5ee 0%,#4fd0b1 35%,#2a9d88 60%,#2a4b8d 85%,#cfeee6 100%)}
.art-costs{left:214px;top:-13px;width:236px;height:239px;background:linear-gradient(140deg,#e7eefb 0%,#f6a7b9 35%,#ee6f8e 55%,#8cc0ef 80%,#23365f 100%)}
.art-secure{left:731px;top:-6px;width:255px;height:240px;background:linear-gradient(150deg,#e9edf3 0%,#f7c948 30%,#2f56a3 55%,#f4b323 80%,#fbd86a 100%)}
.art-extras{left:207px;top:-2px;width:250px;height:193px;background:linear-gradient(135deg,#e8effb 0%,#2f6fd6 40%,#1f3e8a 60%,#f28a3a 80%,#6cc17a 100%)}

/* closing call */
.closing{position:absolute;left:0;top:3225px;width:1200px;text-align:center;color:var(--white)}
.closing-title{font-weight:500;font-size:22px;line-height:36px}
.closing-text{font-weight:300;font-size:13px;margin-top:6px}
.closing .cta-button{left:508px;top:99px;width:184px;height:33px}

/* footer */
.site-footer .brand{top:3523px;color:var(--white)}
.social-links{position:absolute;left:826px;top:3532px;display:flex;gap:26px}
.social-links span{width:14px;height:14px;border-radius:50%;border:1.5px solid rgba(255,255,255,.85)}
.copyright{position:absolute;left:0;top:3627px;width:1200px;text-align:center;font-size:11px;color:rgba(255,255,255,.75)}
</style>
</head>
<body>

<svg class="backdrop" viewBox="0 0 1200 3681" aria-hidden="true">
  <polygon fill="#f1f7fb" points="0,907 600,950 1200,907 1200,1340 600,1383 0,1340"/>
  <polygon fill="#f1f7fb" points="0,1797 600,1840 1200,1797 1200,2229 600,2271 0,2229"/>
  <polygon fill="#f1f7fb" points="0,2686 600,2729 1200,2686 1200,3140 0,3140"/>
  <polygon fill="#1e4fa6" points="0,3121 600,3164 1200,3121 1200,3681 0,3681"/>
  <path fill="#1a4597" d="M0 3440 C100 3395 200 3398 300 3428 S500 3472 600 3432 S800 3388 900 3418 S1100 3470 1200 3422 V3681 H0 Z"/>
  <rect fill="#173f8c" x="0" y="3470" width="1200" height="211"/>
  <line x1="0" y1="3593" x2="1200" y2="3593" stroke="rgba(255,255,255,.14)"/>
</svg>

<header class="site-header">
  <div class="brand"><span class="brand-mark"></span>Harbor Lumen</div>
  <nav class="main-nav">
    <a href="#" class="is-active">Home</a>
    <a href="#">Flavors</a>
  </nav>
  <a class="header-cta" href="#">Configure Now!</a>
</header>

<section class="hero">
  <div class="hero-photo" role="img" aria-label="Photo of smiling students working at a desk in a classroom"></div>
  <svg class="hero-panel" viewBox="0 0 1200 435" aria-hidden="true">
    <polygon fill="#1e90f0" points="667,0 1200,0 1200,435 587,435"/>
  </svg>
  <div class="hero-copy">
    <h1 class="hero-title">MANAGED WIRELESS<br>NETWORKS FOR EDUCATION</h1>
    <p class="hero-sub">Don't have to worry about anything</p>
    <a class="cta-button" href="#">
      <span class="cta-icon"><svg width="22" height="22" viewBox="0 0 24 24" fill="none" stroke="#1e90f0" stroke-width="1.4"><circle cx="12" cy="12" r="3.2"/><path d="M12 2.5v3M12 18.5v3M2.5 12h3M18.5 12h3M5.3 5.3l2.1 2.1M16.6 16.6l2.1 2.1M5.3 18.7l2.1-2.1M16.6 7.4l2.1-2.1"/><circle cx="12" cy="12" r="6.5"/></svg></span>
      <span class="cta-label">Configure Now!</span>
    </a>
  </div>
</section>

<main>
  <section class="feature feature--left" style="top:590px">
    <h2 class="feature-title">Real time <strong>Maintenance</strong></h2>
    <p class="feature-text">Lorem Ipsum is simply dummy text of the printing and typesetting<br>industry. Lorem Ipsum has been the industry's standard dummy text<br>ever since the 1500s, when an unknown printer took a galley of type<br>and scrambled it to make a type specimen book.</p>
    <a class="cta-button" href="#"><span class="cta-icon"><svg width="22" height="22" viewBox="0 0 24 24" fill="none" stroke="#1e90f0" stroke-width="1.4"><circle cx="12" cy="12" r="3.2"/><path d="M12 2.5v3M12 18.5v3M2.5 12h3M18.5 12h3M5.3 5.3l2.1 2.1M16.6 16.6l2.1 2.1M5.3 18.7l2.1-2.1M16.6 7.4l2.1-2.1"/><circle cx="12" cy="12" r="6.5"/></svg></span><span class="cta-label">Configure Now!</span></a>
    <div class="feature-divider"></div>
    <div class="feature-art art-maintenance" role="img" aria-label="Illustration of a support team monitoring a network dashboard on a large screen"></div>
    <div class="read-more"><span>+</span>Read more</div>
  </section>

  <section class="feature feature--right" style="top:1034px">
    <h2 class="feature-title">Service <strong>Range</strong></h2>
    <p class="feature-text">Lorem Ipsum is simply dummy text of the printing and typesetting<br>industry. Lorem Ipsum has been the industry's standard dummy text<br>ever since the 1500s, when an unknown printer took a galley of type<br>and scrambled it to make a type specimen book.</p>
    <a class="cta-button" href="#"><span class="cta-icon"><svg width="22" height="22" viewBox="0 0 24 24" fill="none" stroke="#1e90f0" stroke-width="1.4"><circle cx="12" cy="12" r="3.2"/><path d="M12 2.5v3M12 18.5v3M2.5 12h3M18.5 12h3M5.3 5.3l2.1 2.1M16.6 16.6l2.1 2.1M5.3 18.7l2.1-2.1M16.6 7.4l2.1-2.1"/><circle cx="12" cy="12" r="6.5"/></svg></span><span class="cta-label">Configure Now!</span></a>
    <div class="feature-divider"></div>
    <div class="feature-art art-range" role="img" aria-label="Illustration of a team working among large gears"></div>
    <div class="read-more"><span>+</span>Read more</div>
  </section>

  <section class="feature feature--left" style="top:1473px">
    <h2 class="feature-title"><strong>Speed</strong></h2>
    <p class="feature-text">Lorem Ipsum is simply dummy text of the printing and typesetting<br>industry. Lorem Ipsum has been the industry's standard dummy text<br>ever since the 1500s, when an unknown printer took a galley of type<br>and scrambled it to make a type specimen book.</p>
    <a class="cta-button" href="#"><span class="cta-icon"><svg width="22" height="22" viewBox="0 0 24 24" fill="none" stroke="#1e90f0" stroke-width="1.4"><circle cx="12" cy="12" r="3.2"/><path d="M12 2.5v3M12 18.5v3M2.5 12h3M18.5 12h3M5.3 5.3l2.1 2.1M16.6 16.6l2.1 2.1M5.3 18.7l2.1-2.1M16.6 7.4l2.1-2.1"/><circle cx="12" cy="12" r="6.5"/></svg></span><span class="cta-label">Configure Now!</span></a>
    <div class="feature-divider"></div>
    <div class="feature-art art-speed" role="img" aria-label="Illustration of a globe connected to devices in a fast network"></div>
    <div class="read-more"><span>+</span>Read more</div>
  </section>

  <section class="feature feature--right" style="top:1924px">
    <h2 class="feature-title">Manageable <strong>Costs</strong></h2>
    <p class="feature-text">Lorem Ipsum is simply dummy text of the printing and typesetting<br>industry. Lorem Ipsum has been the industry's standard dummy text<br>ever since the 1500s, when an unknown printer took a galley of type<br>and scrambled it to make a type specimen book.</p>
    <a class="cta-button" href="#"><span class="cta-icon"><svg width="22" height="22" viewBox="0 0 24 24" fill="none" stroke="#1e90f0" stroke-width="1.4"><circle cx="12" cy="12" r="3.2"/><path d="M12 2.5v3M12 18.5v3M2.5 12h3M18.5 12h3M5.3 5.3l2.1 2.1M16.6 16.6l2.1 2.1M5.3 18.7l2.1-2.1M16.6 7.4l2.1-2.1"/><circle cx="12" cy="12" r="6.5"/></svg></span><span class="cta-label">Configure Now!</span></a>
    <div class="feature-divider"></div>
    <div class="feature-art art-costs" role="img" aria-label="Illustration of a person choosing options on a large tablet"></div>
    <div class="read-more"><span>+</span>Read more</div>
  </section>

  <section class="feature feature--left" style="top:2363px">
    <h2 class="feature-title">Protected <strong>And Secure</strong></h2>
    <p class="feature-text">Lorem Ipsum is simply dummy text of the printing and typesetting<br>industry. Lorem Ipsum has been the industry's standard dummy text<br>ever since the 1500s, when an unknown printer took a galley of type<br>and scrambled it to make a type specimen book.</p>
    <a class="cta-button" href="#"><span class="cta-icon"><svg width="22" height="22" viewBox="0 0 24 24" fill="none" stroke="#1e90f0" stroke-width="1.4"><circle cx="12" cy="12" r="3.2"/><path d="M12 2.5v3M12 18.5v3M2.5 12h3M18.5 12h3M5.3 5.3l2.1 2.1M16.6 16.6l2.1 2.1M5.3 18.7l2.1-2.1M16.6 7.4l2.1-2.1"/><circle cx="12" cy="12" r="6.5"/></svg></span><span class="cta-label">Configure Now!</span></a>
    <div class="feature-divider"></div>
    <div class="feature-art art-secure" role="img" aria-label="Illustration of a computer protected by a shield and padlock"></div>
    <div class="read-more"><span>+</span>Read more</div>
  </section>

  <section class="feature feature--right" style="top:2816px">
    <h2 class="feature-title"><strong>Extras</strong></h2>
    <p class="feature-text">Lorem Ipsum is simply dummy text of the printing and typesetting<br>industry. Lorem Ipsum has been the industry's standard dummy text<br>ever since the 1500s, when an unknown printer took a galley of type<br>and scrambled it to make a type specimen book.</p>
    <a class="cta-button" href="#"><span class="cta-icon"><svg width="22" height="22" viewBox="0 0 24 24" fill="none" stroke="#1e90f0" stroke-width="1.4"><circle cx="12" cy="12" r="3.2"/><path d="M12 2.5v3M12 18.5v3M2.5 12h3M18.5 12h3M5.3 5.3l2.1 2.1M16.6 16.6l2.1 2.1M5.3 18.7l2.1-2.1M16.6 7.4l2.1-2.1"/><circle cx="12" cy="12" r="6.5"/></svg></span><span class="cta-label">Configure Now!</span></a>
    <div class="feature-divider"></div>
    <div class="feature-art art-extras" role="img" aria-label="Illustration of people around a laptop with extra connected services"></div>
    <div class="read-more"><span>+</span>Read more</div>
  </section>

  <section class="closing">
    <h2 class="closing-title">Immediately A Statement Of Costs</h2>
    <p class="closing-text">Lorem Ipsum is simply dummy text of the printing and typesetting</p>
    <a class="cta-button" href="#"><span class="cta-icon"><svg width="22" height="22" viewBox="0 0 24 24" fill="none" stroke="#1e90f0" stroke-width="1.4"><circle cx="12" cy="12" r="3.2"/><path d="M12 2.5v3M12 18.5v3M2.5 12h3M18.5 12h3M5.3 5.3l2.1 2.1M16.6 16.6l2.1 2.1M5.3 18.7l2.1-2.1M16.6 7.4l2.1-2.1"/><circle cx="12" cy="12" r="6.5"/></svg></span><span class="cta-label">Configure Now!</span></a>
  </section>
</main>

<footer class="site-footer">
  <div class="brand"><span class="brand-mark"></span>Harbor Lumen</div>
  <div class="social-links" aria-label="Social links"><span></span><span></span><span></span><span></span></div>
  <p class="copyright">© 2020 Harbor Lumen</p>
</footer>

</body>
</html>
```